Brindle Property Management Vendor Recruiting Email

We need a digital flyer to email and post on Social media to attract new vendors to our website to apply to complete maintenance work on our clients homes. I have one flyer we had produced recently that we are un-happy with. It is attached.

The example given is what we do not want!! We do not want any of the pictures used from the existing one

Target Market(s)

Construction companies and handyman

Industry/Entity Type

Residential maintenance and repairs

Requirements
Must have
• Join our team as the header not become a vendor

```html
<!DOCTYPE html>
<html lang="en">
<head>
<meta charset="utf-8">
<title>Brindle Property Management – Join Our Team</title>
<link href="https://fonts.googleapis.com/css2?family=Montserrat:wght@300;400;600;700;800&family=Roboto:wght@400;500;700&display=swap" rel="stylesheet">
<style>
  :root{
    --ink:#1a1626;
    --white:#ffffff;
    --purple:#9c4fa0;
    --purple-soft:#c78fcc;
    --tick:#a0449f;
    --sky:#13bdf0;
    --sky-light:#5fd6f7;
    --text-dark:#2b2b3a;
    --rule:#5b5868;
  }
  *{margin:0;padding:0;box-sizing:border-box}
  html,body{width:925px;height:1200px;overflow:hidden;background:var(--ink)}
  .flyer{position:relative;width:925px;height:1200px;overflow:hidden;background:var(--ink);font-family:'Roboto',sans-serif;color:var(--white)}

  .photo{position:absolute;inset:0}
  .photo--worker{clip-path:polygon(220px 0,925px 0,925px 176px,621px 797px);
    background:linear-gradient(160deg,#e9dcc4 0%,#d9b98a 30%,#2d3a85 58%,#26306e 80%,#c98b3a 100%)}
  .photo--drill{clip-path:polygon(925px 176px,925px 1200px,830px 1200px,621px 797px);
    background:linear-gradient(170deg,#e8e6e6 0%,#d8cfc7 40%,#c58a3c 62%,#e9e7e5 85%,#f4f3f2 100%)}
  .photo-divider{position:absolute;inset:0;pointer-events:none}

  .brand{position:absolute;left:92px;top:92px;width:160px;text-align:center}
  .brand__mark{width:26px;height:26px;background:var(--sky);margin:0 auto 12px}
  .brand__name{font-family:'Montserrat',sans-serif;font-weight:700;font-size:28px;letter-spacing:3px;line-height:1}
  .brand__sub{font-family:'Montserrat',sans-serif;font-weight:700;font-size:9.5px;letter-spacing:1.6px;margin-top:6px}

  .headline{position:absolute;left:0;top:0;width:925px;height:530px}
  .headline text{font-family:'Montserrat',sans-serif;font-weight:700;fill:var(--white)}

  .requirements__band{position:absolute;left:62px;top:540px;width:500px;height:103px;
    clip-path:polygon(0 0,435px 0,485px 103px,0 103px);
    background:linear-gradient(180deg,var(--purple) 0%,var(--purple) 80%,var(--purple-soft) 100%)}
  .requirements__title{position:absolute;left:24px;top:14px;font-family:'Montserrat',sans-serif;font-weight:700;font-size:40px;letter-spacing:6.4px;line-height:1}
  .requirements__subtitle{position:absolute;left:24px;top:64px;font-family:'Montserrat',sans-serif;font-weight:400;font-size:24px;letter-spacing:9.4px;line-height:1}
  .requirements__list{position:absolute;left:62px;top:643px;width:560px;height:154px;background:var(--white);
    clip-path:polygon(0 0,485px 0,559px 154px,0 154px);list-style:none}
  .requirements__item{position:absolute;display:flex;align-items:flex-start;gap:14px;color:var(--text-dark);font-size:15px;line-height:18px;letter-spacing:.3px}
  .requirements__item svg{flex:none;margin-top:2px}

  .perk{position:absolute;background:linear-gradient(100deg,var(--sky) 0%,var(--sky) 55%,var(--sky-light) 100%)}
  .perk--approval{left:62px;top:808px;width:257px;height:120px}
  .perk--volume{left:328px;top:808px;width:360px;height:120px;clip-path:polygon(0 0,296px 0,360px 120px,0 120px)}
  .perk--materials{left:62px;top:938px;width:257px;height:119px}
  .perk--deposit{left:328px;top:938px;width:428px;height:119px;clip-path:polygon(0 0,364px 0,428px 119px,0 119px)}
  .perk svg{position:absolute}
  .perk__big{position:absolute;font-weight:700;line-height:1}
  .perk__small{position:absolute;font-weight:500;line-height:1.2}

  .contact__call{position:absolute;left:76px;top:1083px;display:flex;align-items:center;gap:14px}
  .contact__label{font-family:'Montserrat',sans-serif;font-weight:700;font-size:22px;letter-spacing:3.5px}
  .contact__phone{font-family:'Montserrat',sans-serif;font-weight:700;font-size:40px;letter-spacing:2px;margin-left:-2px}
  .contact__rule{position:absolute;left:76px;top:1134px;width:572px;height:1px;background:var(--rule)}
  .contact__web{position:absolute;left:76px;top:1146px;display:flex;align-items:center;gap:14px;font-family:'Montserrat',sans-serif;font-weight:400;font-size:23px;letter-spacing:4.3px}
  .footer-strip{position:absolute;left:0;top:1189px;width:830px;height:11px;background:linear-gradient(90deg,var(--purple),var(--sky));clip-path:polygon(0 0,824px 0,830px 11px,0 11px)}
</style>
</head>
<body>
<main class="flyer">
  <div class="photo photo--worker" role="img" aria-label="Smiling contractor in a yellow hard hat and navy polo on a building site"></div>
  <div class="photo photo--drill" role="img" aria-label="Close-up of hands using an orange cordless drill on a white surface"></div>
  <svg class="photo-divider" width="925" height="1200"><line x1="925" y1="176" x2="621" y2="797" stroke="#fff" stroke-width="4"/></svg>

  <div class="brand">
    <div class="brand__mark"></div>
    <div class="brand__name">BRINDLE</div>
    <div class="brand__sub">PROPERTY MANAGEMENT</div>
  </div>

  <svg class="headline" width="925" height="530">
    <text x="63" y="329" font-size="124" textLength="592" lengthAdjust="spacingAndGlyphs">JOIN OUR</text>
    <text x="52" y="514" font-size="222" textLength="660" lengthAdjust="spacingAndGlyphs">TEAM</text>
  </svg>

  <section class="requirements">
    <div class="requirements__band">
      <h2 class="requirements__title">REQUIREMENTS</h2>
      <p class="requirements__subtitle">TO BECOME A VENDOR</p>
    </div>
    <ul class="requirements__list">
      <li class="requirements__item" style="left:28px;top:16px"><svg width="14" height="14" viewBox="0 0 14 14"><rect x="1" y="1" width="12" height="12" fill="none" stroke="#a0449f" stroke-width="2"/><path d="M3.5 6.5l3 3 5.5-7" fill="none" stroke="#a0449f" stroke-width="2.4"/></svg><span>Auto insurance</span></li>
      <li class="requirements__item" style="left:28px;top:62px"><svg width="14" height="14" viewBox="0 0 14 14"><rect x="1" y="1" width="12" height="12" fill="none" stroke="#a0449f" stroke-width="2"/><path d="M3.5 6.5l3 3 5.5-7" fill="none" stroke="#a0449f" stroke-width="2.4"/></svg><span>Certificate of general<br>liability insurance</span></li>
      <li class="requirements__item" style="left:28px;top:119px"><svg width="14" height="14" viewBox="0 0 14 14"><rect x="1" y="1" width="12" height="12" fill="none" stroke="#a0449f" stroke-width="2"/><path d="M3.5 6.5l3 3 5.5-7" fill="none" stroke="#a0449f" stroke-width="2.4"/></svg><span>Coverage area</span></li>
      <li class="requirements__item" style="left:238px;top:15px"><svg width="14" height="14" viewBox="0 0 14 14"><rect x="1" y="1" width="12" height="12" fill="none" stroke="#a0449f" stroke-width="2"/><path d="M3.5 6.5l3 3 5.5-7" fill="none" stroke="#a0449f" stroke-width="2.4"/></svg><span>Workman's compensation or<br>state issued exemption letter</span></li>
      <li class="requirements__item" style="left:238px;top:63px"><svg width="14" height="14" viewBox="0 0 14 14"><rect x="1" y="1" width="12" height="12" fill="none" stroke="#a0449f" stroke-width="2"/><path d="M3.5 6.5l3 3 5.5-7" fill="none" stroke="#a0449f" stroke-width="2.4"/></svg><span>Drive licence or state<br>issued ID card</span></li>
      <li class="requirements__item" style="left:238px;top:118px"><svg width="14" height="14" viewBox="0 0 14 14"><rect x="1" y="1" width="12" height="12" fill="none" stroke="#a0449f" stroke-width="2"/><path d="M3.5 6.5l3 3 5.5-7" fill="none" stroke="#a0449f" stroke-width="2.4"/></svg><span>Any specialty licenses</span></li>
    </ul>
  </section>

  <section class="perks">
    <div class="perk perk--approval">
      <svg style="left:25px;top:38px" width="42" height="42" viewBox="0 0 42 42"><circle cx="21" cy="21" r="18.5" fill="none" stroke="#fff" stroke-width="3.5"/><path d="M13 21.5l6 6 10-11" fill="none" stroke="#fff" stroke-width="3.5" stroke-linecap="round" stroke-linejoin="round"/></svg>
      <span class="perk__big" style="left:89px;top:24px;font-size:48px">95%</span>
      <span class="perk__small" style="left:89px;top:78px;font-size:12.5px">approval rating on all<br>submitted estimates.</span>
    </div>
    <div class="perk perk--volume">
      <svg style="left:24px;top:37px" width="58" height="52" viewBox="0 0 58 52"><g fill="none" stroke="#fff" stroke-width="2.6" stroke-linejoin="round"><path d="M29 3L55 15 29 27 3 15z"/><path d="M7 23L3 25l26 12 26-12-4-2"/><path d="M7 33L3 35l26 12 26-12-4-2"/></g></svg>
      <span class="perk__small" style="left:102px;top:34px;font-size:16px;font-weight:400;letter-spacing:.5px">Guaranteed</span>
      <span class="perk__big" style="left:102px;top:58px;font-size:31px">Work Volume.</span>
    </div>
    <div class="perk perk--materials">
      <svg style="left:17px;top:40px" width="52" height="52" viewBox="0 0 52 52"><g fill="none" stroke="#fff" stroke-width="2.4" stroke-linejoin="round"><path d="M32 4H8v44h10"/><path d="M32 4v8h8v8"/><path d="M8 4L3 10v38h5"/><rect x="21" y="20" width="30" height="30" rx="2"/><rect x="25" y="24" width="22" height="6"/><rect x="25" y="34" width="5" height="4"/><rect x="33" y="34" width="5" height="4"/><rect x="41" y="34" width="5" height="4"/><rect x="25" y="42" width="5" height="4"/><rect x="33" y="42" width="5" height="4"/><rect x="41" y="42" width="5" height="4"/></g></svg>
      <span class="perk__big" style="left:89px;top:12px;font-size:21px;line-height:1.12">Material<br>Purchasing<br>Program</span>
      <span class="perk__small" style="left:89px;top:86px;font-size:10.5px;font-weight:400">to help vendors with low capital<br>or no or bad credit.</span>
    </div>
    <div class="perk perk--deposit">
      <svg style="left:15px;top:37px" width="68" height="50" viewBox="0 0 68 50"><g fill="none" stroke="#fff" stroke-width="2.4" stroke-linejoin="round"><rect x="2" y="12" width="30" height="30"/><rect x="10" y="8" width="54" height="34"/><rect x="16" y="4" width="50" height="44"/><circle cx="42" cy="26" r="7"/><path d="M24 28l8-14 6 3"/><path d="M58 20v12"/></g><rect x="8" y="30" width="3" height="3" fill="#fff"/></svg>
      <span class="perk__small" style="left:102px;top:22px;font-size:16px;font-weight:400;letter-spacing:.5px">Weekly Secure</span>
      <span class="perk__big" style="left:102px;top:46px;font-size:31px">Direct Deposit</span>
      <span class="perk__small" style="left:102px;top:84px;font-size:16px;font-weight:400;letter-spacing:.6px">with net 30 payment terms.</span>
    </div>
  </section>

  <footer class="contact">
    <div class="contact__call">
      <svg width="22" height="22" viewBox="0 0 24 24"><path fill="#fff" d="M6.6 10.8a15.2 15.2 0 0 0 6.6 6.6l2.2-2.2c.3-.3.7-.4 1-.2 1.1.4 2.3.6 3.6.6.6 0 1 .4 1 1V20c0 .6-.4 1-1 1A17 17 0 0 1 3 4c0-.6.4-1 1-1h3.5c.6 0 1 .4 1 1 0 1.3.2 2.5.6 3.6.1.3 0 .7-.2 1z"/></svg>
      <span class="contact__label">CALL US NOW!</span>
      <span class="contact__phone">555-214-3690</span>
    </div>
    <div class="contact__rule"></div>
    <div class="contact__web">
      <svg width="24" height="24" viewBox="0 0 24 24"><g fill="none" stroke="#fff" stroke-width="1.5"><circle cx="12" cy="12" r="10.5"/><ellipse cx="12" cy="12" rx="4.5" ry="10.5"/><path d="M1.5 12h21M3 6.5h18M3 17.5h18"/></g></svg>
      <span>www.brindlepropertymanagement.com</span>
    </div>
    <div class="footer-strip"></div>
  </footer>
</main>
</body>
</html>
```